A Tolland Grad

This poster is to show how we want the world to view our high school students when the graduate. The values and lessons they should live by.
I'd like for the middle to say "A TOLLAND GRAD IS..." and it should be surrounded by the following values:
Never Quits
Doesn't Put Others Down
Respects Everyone
Learns from their mistakes
Takes action
Always looks to Improve
Looks to the future
Puts others' needs before our own

and the final emotion one should have more emphasis....
will always be a part of Tolland

I want it to look cool and sleek, not just listed out. Maybe a thought bubble or something like that. Please use school colors and use the school logo

```html
<!DOCTYPE html>
<html lang="en">
<head>
<meta charset="utf-8">
<title>A Tolland Grad</title>
<link rel="stylesheet" href="https://fonts.googleapis.com/css2?family=Montserrat:wght@500;800;900&display=swap">
<style>
  :root {
    --page-bg: #e4e3e1;
    --poster-bg: #efeeec;
    --gold: #dcae26;
    --navy: #2f2a7c;
    --ink: #2e2608;
    --white: #ffffff;
  }
  * { box-sizing: border-box; margin: 0; padding: 0; }
  html, body {
    width: 1200px; height: 920px; overflow: hidden;
    background: var(--page-bg);
    font-family: "Montserrat", Arial, sans-serif;
  }
  .poster {
    position: absolute; left: 330px; top: 30px;
    width: 540px; height: 860px;
    background: var(--poster-bg);
    overflow: hidden;
  }
  .bubble {
    position: absolute; left: 50px; top: 50px;
    width: 450px; height: 500px;
  }
  .bubble-shape { position: absolute; left: 0; top: 0; overflow: visible; }
  .emblem-art {
    position: absolute; left: 50px; top: 120px;
    width: 95px; height: 175px;
    background: linear-gradient(160deg, #fff8e6 0%, #f3e2b0 100%);
    border-radius: 40px 40px 20px 50px;
    opacity: .9;
  }
  .headline {
    position: absolute; left: 38px; top: 312px;
    color: var(--white);
    font-weight: 900; font-size: 27px; line-height: 1.05;
    letter-spacing: -0.5px; text-transform: uppercase;
  }
  .values { list-style: none; }
  .value {
    position: absolute;
    color: var(--ink); font-weight: 500; font-size: 13px; line-height: 1.2;
    white-space: nowrap;
  }
  .value--wrap { white-space: normal; width: 170px; }
  .closing {
    position: absolute; left: 276px; top: 560px;
    color: var(--navy); font-weight: 900; font-size: 17px; line-height: 1.1;
    text-transform: uppercase; letter-spacing: -0.2px;
  }
  .school-mark {
    position: absolute; left: 0; right: 0; top: 680px;
    display: flex; align-items: center; justify-content: center; gap: 14px;
  }
  .school-mark__dot {
    width: 54px; height: 54px; border-radius: 50%;
    background: var(--gold); border: 4px solid var(--navy);
  }
  .school-mark__name {
    color: var(--navy); font-weight: 800; font-size: 20px;
  }
  .base-bar {
    position: absolute; left: 340px; bottom: 0;
    width: 190px; height: 6px; background: var(--navy);
  }
</style>
</head>
<body>
  <main class="poster">
    <section class="bubble">
      <svg class="bubble-shape" width="450" height="560" viewBox="0 0 450 560" aria-hidden="true">
        <path d="M24 0 H426 A24 24 0 0 1 450 24 V476 A24 24 0 0 1 426 500 H225 V556 L196 500 H24 A24 24 0 0 1 0 476 V24 A24 24 0 0 1 24 0 Z" fill="var(--gold)"/>
        <g stroke="var(--ink)" stroke-width="1.2" fill="none">
          <line x1="145" y1="250" x2="205" y2="250"/>
          <line x1="205" y1="82" x2="205" y2="418"/>
          <line x1="205" y1="82" x2="215" y2="82"/>
          <line x1="205" y1="130" x2="219" y2="130"/>
          <line x1="205" y1="176" x2="221" y2="176"/>
          <line x1="205" y1="222" x2="225" y2="222"/>
          <line x1="205" y1="270" x2="227" y2="270"/>
          <line x1="205" y1="318" x2="231" y2="318"/>
          <line x1="205" y1="366" x2="235" y2="366"/>
          <line x1="205" y1="418" x2="239" y2="418"/>
        </g>
      </svg>
      <div class="emblem-art" role="img" aria-label="White eagle mascot illustration"></div>
      <h1 class="headline">A<br>Tolland<br>Grad<br>Is...</h1>
      <ul class="values">
        <li class="value" style="left:217px; top:74px;">Never Quits</li>
        <li class="value" style="left:221px; top:122px;">Doesn't Put Others Down</li>
        <li class="value" style="left:223px; top:168px;">Respects Everyone</li>
        <li class="value" style="left:227px; top:214px;">Learns from their mistakes</li>
        <li class="value" style="left:229px; top:262px;">Takes action</li>
        <li class="value" style="left:233px; top:310px;">Always looks to Improve</li>
        <li class="value" style="left:237px; top:358px;">Looks to the future</li>
        <li class="value value--wrap" style="left:241px; top:410px;">Puts others' needs before our own</li>
      </ul>
    </section>
    <p class="closing">Will always<br>be a part of Tolland</p>
    <div class="school-mark">
      <span class="school-mark__dot"></span>
      <span class="school-mark__name">Tolland Academy</span>
    </div>
    <div class="base-bar"></div>
  </main>
</body>
</html>
```